Business Card Design Project

We need a double-sided business card design for our e-commerce company. Be as creative as you can.

Reason: Change of logo

Target Market(s)

Business owners

Industry/Entity Type

E-Commerce

Requirements
Must have
• Name (editable)
Mobile number -editable
www.trizvo.com - MUST STAND OUT ALONE
Office address:
27 Pellow Road
#09-04 Corbell Tower
Singapore 058214

```html
<!DOCTYPE html>
<html lang="en">
<head>
<meta charset="utf-8">
<title>Trizvo Business Card</title>
<link rel="stylesheet" href="https://fonts.googleapis.com/css2?family=Cinzel:wght@400;700&display=swap">
<style>
  :root {
    --canvas: #e9e6e1;
    --card: #121212;
    --card-edge: #1c1c1c;
    --orange: #f26a1b;
    --orange-deep: #c9530f;
    --blue: #2f6fc4;
    --blue-light: #5cb4f0;
    --text-light: #d8d0c4;
  }
  * { box-sizing: border-box; margin: 0; padding: 0; }
  html, body {
    width: 1200px; height: 1200px; overflow: hidden;
    background: var(--canvas);
    font-family: "Cinzel", serif;
  }
  .canvas {
    position: relative; width: 1200px; height: 1200px;
    display: flex; flex-direction: column; align-items: center; justify-content: center; gap: 70px;
  }
  .card {
    position: relative; width: 900px; height: 514px;
    background: radial-gradient(ellipse at 50% 40%, var(--card-edge), var(--card) 70%);
    box-shadow: 0 10px 30px rgba(0,0,0,0.3);
    overflow: hidden;
  }
  .stripes {
    position: absolute; left: 0; right: 0; bottom: 28px;
    display: flex; flex-direction: column; gap: 4px;
  }
  .stripe { display: flex; height: 8px; }
  .stripe .seg-orange { flex: 0 0 74%; background: var(--orange); }
  .stripe .seg-blue { flex: 1; background: var(--blue); }
  .stripe.dim .seg-orange { background: var(--orange-deep); }

  /* front */
  .card-front .brand {
    position: absolute; top: 120px; left: 0; right: 0; text-align: center;
    font-size: 150px; font-weight: 700; color: var(--orange); letter-spacing: 4px;
    text-transform: lowercase;
  }
  .card-front .web {
    position: absolute; top: 370px; left: 0; right: 0; text-align: center;
    font-size: 24px; color: var(--orange); letter-spacing: 2px;
  }

  /* back */
  .card-back .brand-small {
    position: absolute; top: 40px; right: 60px;
    font-size: 40px; font-weight: 700; color: var(--orange); text-transform: lowercase;
  }
  .contact { position: absolute; left: 56px; top: 80px; color: var(--text-light); }
  .contact .name { font-size: 34px; color: var(--blue-light); letter-spacing: 1px; }
  .contact .role { font-size: 18px; color: var(--orange); margin-top: 4px; }
  .contact .phones { margin-top: 70px; font-size: 17px; line-height: 32px; }
  .contact .phones .label { color: var(--blue-light); margin-right: 14px; }
  .contact .address { margin-top: 52px; font-size: 17px; line-height: 24px; }
  .card-back .web {
    position: absolute; right: 60px; top: 390px;
    font-size: 20px; color: var(--orange); letter-spacing: 1px;
  }
</style>
</head>
<body>
<main class="canvas">
  <section class="card card-front">
    <div class="brand">trizvo</div>
    <div class="web">WWW.TRIZVO.COM</div>
    <div class="stripes">
      <div class="stripe"><span class="seg-orange"></span><span class="seg-blue"></span></div>
      <div class="stripe dim"><span class="seg-orange"></span><span class="seg-blue"></span></div>
      <div class="stripe"><span class="seg-orange"></span><span class="seg-blue"></span></div>
    </div>
  </section>

  <section class="card card-back">
    <div class="brand-small">trizvo</div>
    <div class="contact">
      <div class="name">Marcus Tan</div>
      <div class="role">Founder/Owner</div>
      <div class="phones">
        <div><span class="label">P:</span>013572-046810</div>
        <div><span class="label">F:</span>015683-047920</div>
      </div>
      <div class="address">
        <div>27 Pellow Road</div>
        <div>#09-04 Corbell Tower</div>
        <div>Singapore 058214</div>
      </div>
    </div>
    <div class="web">WWW.TRIZVO.COM</div>
    <div class="stripes">
      <div class="stripe"><span class="seg-orange"></span><span class="seg-blue"></span></div>
      <div class="stripe dim"><span class="seg-orange"></span><span class="seg-blue"></span></div>
      <div class="stripe"><span class="seg-orange"></span><span class="seg-blue"></span></div>
    </div>
  </section>
</main>
</body>
</html>
```